Professional Business Card for Luxury Hotel & Resort Development Firm. Advisory firm

Project Overview: We are a specialized advisory firm focused on Hotel & Resort Development. Our clients are high-net-worth investors and major hospitality brands.

Design Requirements:

Style: Minimalist, sophisticated, and trustworthy. We want to avoid looking too "corporate" or "dry"—it should feel premium.

Key Elements: Please incorporate our logo [もしロゴがあれば] and emphasize a clean layout with plenty of white space.

Color Palette: We prefer Grey and White or Black and White to evoke a sense of luxury and stability.

Typography: Professional garamond, or sans-serif or elegant serif fonts

Goal: The card should feel substantial and high-end when handed to a client, reflecting our expertise in multi-million dollar developments.
Updates

I am currently on a business trip for field research and have limited access to my desktop. Additionally, I have just provided detailed technical feedback to a designer and am waiting for their refined proposals. To ensure the final logo meets the high standards of my new advisory firm, I would like to extend the deadline by 7 days. Thank you for your support.

Target Market(s)

High-net-worth investors, luxury hospitality brands, and real estate developers.

Contact Information for Business Card

Firm Name: Larkfield Counsel Partners, My Name: Kenji Morisawa, Title: Founder, Address 5-7-4 Kitakawabe Asahi Yokohama Japan 241-0815, email address: kmorisawa@larkfieldcp.com, Tel: +81 80-4821-3357. Front Site (Primary): Japanese translation of the back side, Please use a clean Japanese font (like Mincho) that complements the Garmond on the English side Back side: English. Note for Japanese text: since the frond side is the main fae, please ensure the layout is clean and professional. Please use a high-quality Mincho ( Serif-style) font for Japanese to mach the Garmond used on the English side. Text for Front side (Japanese) Larkfield Counsel Partners, 役職:代表、森沢健二、241-0815 横浜市旭区北川辺5-7-4. Name of the firm can stay in English.

Font styles to use
Other font styles liked:
• Font Preference: Please use Garamond for all text to maintain a consistent, elegant, and classic professional look.

Requirements
Must have
• Professional and clean layout, high-end feel.
Nice to have
• Minimalist design with subtle luxury accents.

```html
<!DOCTYPE html>
<html lang="en">
<head>
<meta charset="utf-8">
<title>Larkfield Counsel Partners — Business Card</title>
<link rel="stylesheet" href="https://fonts.googleapis.com/css2?family=EB+Garamond:ital,wght@0,400;1,400&family=Shippori+Mincho:wght@400&display=swap">
<style>
  :root {
    --backdrop: #e7e7e7;
    --taupe: #bcb3a5;
    --paper: #f7f7f7;
    --ink-light: #ffffff;
  }
  html, body {
    margin: 0;
    padding: 0;
    overflow: hidden;
  }
  .canvas {
    position: relative;
    width: 1200px;
    height: 1067px;
    background: var(--backdrop);
    overflow: hidden;
    font-family: "EB Garamond", Garamond, serif;
  }
  .swatch {
    position: absolute;
    left: 0;
    width: 17px;
    height: 100px;
  }
  .swatch--taupe { top: 50px; background: var(--taupe); }
  .swatch--paper { top: 150px; background: var(--paper); }

  .brand-sample {
    position: absolute;
    left: 50px;
    top: 120px;
    width: 170px;
    text-align: center;
    color: var(--taupe);
    font-size: 24px;
    letter-spacing: 0.12em;
    line-height: 1.15;
  }

  .card {
    position: absolute;
    border-radius: 34px;
  }
  .card--front {
    left: 331px;
    top: 100px;
    width: 671px;
    height: 406px;
    background: var(--taupe);
    color: var(--ink-light);
  }
  .card--back {
    left: 332px;
    top: 561px;
    width: 667px;
    height: 403px;
    background: var(--paper);
  }

  .holder {
    position: absolute;
    right: 51px;
    top: 46px;
    text-align: right;
  }
  .holder__name-jp {
    font-family: "Shippori Mincho", serif;
    font-size: 36px;
    letter-spacing: 0.06em;
    line-height: 1;
    margin: 0;
  }
  .holder__name-en {
    font-size: 19px;
    letter-spacing: 0.16em;
    line-height: 1;
    margin: 6px 0 0;
  }
  .holder__title {
    font-size: 12px;
    letter-spacing: 0.14em;
    line-height: 1;
    margin: 6px 0 0;
  }

  .wordmark {
    position: absolute;
    left: 50px;
    bottom: 50px;
    color: var(--ink-light);
    text-align: center;
  }
  .wordmark__primary {
    display: block;
    font-size: 29px;
    letter-spacing: 0.14em;
    line-height: 1;
  }
  .wordmark__secondary {
    display: block;
    font-size: 11.5px;
    letter-spacing: 0.2em;
    margin-top: 5px;
    line-height: 1;
  }

  .contact {
    position: absolute;
    right: 51px;
    bottom: 52px;
    text-align: right;
    font-style: italic;
  }
  .contact__email {
    font-size: 16.5px;
    letter-spacing: 0.1em;
    line-height: 1;
    margin: 0;
  }
  .contact__phone {
    font-size: 18px;
    letter-spacing: 0.12em;
    line-height: 1;
    margin: 7px 0 0;
  }

  .back-wordmark {
    position: absolute;
    left: 0;
    right: 0;
    top: 50%;
    transform: translateY(-50%);
    text-align: center;
    color: var(--taupe);
  }
  .back-wordmark__primary {
    display: block;
    font-size: 40px;
    letter-spacing: 0.16em;
    line-height: 1;
  }
  .back-wordmark__secondary {
    display: block;
    font-size: 15px;
    letter-spacing: 0.24em;
    margin-top: 8px;
    line-height: 1;
  }
</style>
</head>
<body>
<main class="canvas">
  <div class="swatch swatch--taupe"></div>
  <div class="swatch swatch--paper"></div>

  <div class="brand-sample">LARKFIELD</div>

  <section class="card card--front">
    <div class="holder">
      <p class="holder__name-jp" lang="ja">森沢健二</p>
      <p class="holder__name-en">KENJI MORISAWA</p>
      <p class="holder__title">FOUNDER</p>
    </div>

    <div class="wordmark">
      <span class="wordmark__primary">LARKFIELD</span>
      <span class="wordmark__secondary">COUNSEL PARTNERS</span>
    </div>

    <div class="contact">
      <p class="contact__email">kmorisawa@larkfieldcp.com</p>
      <p class="contact__phone">080-4821-3357</p>
    </div>
  </section>

  <section class="card card--back">
    <div class="back-wordmark">
      <span class="back-wordmark__primary">LARKFIELD</span>
      <span class="back-wordmark__secondary">COUNSEL PARTNERS</span>
    </div>
  </section>
</main>
</body>
</html>
```